Dietitian clinic needs a business card design

We need a business card design for a new dietitian group based in Singapore called "Lantern and Tide". We provide expert, personalised nutrition care to support a wide range of health needs, from chronic conditions to mindful eating. Our team also offers consulting, speaking, and tailored solutions for healthcare providers, organisations, and food services.

Target Market(s)

Adults

Industry/Entity Type

Healthcare

Contact Information for Business Card

Name, position, contact number, email, website address, our logo

Requirements
Nice to have
• Clean, professional but welcoming look

```html
<!DOCTYPE html>
<html lang="en">
<head>
<meta charset="utf-8">
<title>Lantern and Tide – Business Card</title>
<link href="https://fonts.googleapis.com/css2?family=Montserrat:wght@400;500;700&display=swap" rel="stylesheet">
<style>
  :root {
    --backdrop: #2a2725;
    --teal: #265a6e;
    --teal-light: #3e7388;
    --card-white: #ffffff;
    --ink: #2b4f5e;
  }
  * { margin: 0; padding: 0; box-sizing: border-box; }
  html, body {
    width: 1200px; height: 900px; overflow: hidden;
    background: var(--backdrop);
    font-family: "Montserrat", Arial, sans-serif;
  }
  .stage {
    position: relative; width: 1200px; height: 900px;
    display: flex; align-items: center; justify-content: center; gap: 70px;
  }
  .card {
    border-radius: 28px;
    box-shadow: 0 18px 40px rgba(0,0,0,0.45);
    position: relative; overflow: hidden;
  }
  .card-back {
    width: 320px; height: 560px;
    background: var(--teal);
    display: flex; flex-direction: column; align-items: center; justify-content: center; gap: 22px;
  }
  .back-mark-dot {
    width: 56px; height: 56px; border-radius: 50%;
    border: 5px solid var(--teal-light);
  }
  .back-brand {
    color: var(--teal-light);
    font-weight: 700; font-size: 30px; line-height: 1.1; text-align: center;
  }
  .card-front {
    width: 560px; height: 320px;
    background: var(--card-white);
    padding: 30px 36px;
    color: var(--ink);
  }
  .front-brand {
    color: var(--teal);
    font-weight: 700; font-size: 34px; line-height: 1.0;
  }
  .holder-name {
    margin-top: 22px;
    font-weight: 700; font-size: 22px; color: var(--teal);
  }
  .holder-role { font-size: 13px; margin-top: 4px; }
  .address { font-size: 13px; margin-top: 12px; line-height: 1.45; }
  .contact-list { list-style: none; margin-top: 12px; font-size: 13px; line-height: 1.7; }
  .contact-list li { display: flex; align-items: center; gap: 8px; }
  .contact-list svg { width: 12px; height: 12px; fill: var(--teal); flex: none; }
</style>
</head>
<body>
<main class="stage">
  <section class="card card-back">
    <div class="back-mark-dot"></div>
    <div class="back-brand">Lantern<br>&amp; Tide</div>
  </section>

  <section class="card card-front">
    <div class="front-brand">Lantern<br>&amp; Tide</div>
    <h1 class="holder-name">Daniel Whitford</h1>
    <p class="holder-role">Managing Director</p>
    <p class="address">Your address, City<br>State, Zip 1234</p>
    <ul class="contact-list">
      <li><svg viewBox="0 0 24 24"><path d="M6.6 10.8a15.1 15.1 0 0 0 6.6 6.6l2.2-2.2a1 1 0 0 1 1-.25 11.4 11.4 0 0 0 3.6.57 1 1 0 0 1 1 1V20a1 1 0 0 1-1 1A17 17 0 0 1 3 4a1 1 0 0 1 1-1h3.5a1 1 0 0 1 1 1c0 1.25.2 2.45.57 3.57a1 1 0 0 1-.25 1z"/></svg>123 456 789</li>
      <li><svg viewBox="0 0 24 24"><path d="M2 5h20v14H2z M2 5l10 8 10-8" /></svg>info@yourmail.com</li>
      <li><svg viewBox="0 0 24 24"><circle cx="12" cy="12" r="10"/></svg>www.yourwebsite.com</li>
    </ul>
  </section>
</main>
</body>
</html>
```